TRV Collection and Shipping Info Sheet

I need to convert an existing rather plain-looking MS Word doc (see attached file Fecal Sample Collection and Shipping Information V2.0.doc) into a visually appealing, professional-looking doc that reflects my current brand’s look and feel (Retail Kit Cover V1.8.pdf). At the same time, I am open to looking at improving on my brand’s look.

Target Market(s)

Horse owners, Barn Managers, Equine Veterinarians

Industry/Entity Type

Horseback Riding

Font styles to use
Sans Serif

Requirements
Must have
• Must be able to fit attached content on 2 pages (1 double signed 8x11 pdf - NOT a trifold doc). Must use Clearfield Pasture Labs brand standards for following colors listed:
• - lime green color: C: 75 Y: 100 or R 57 G 181 B 74 (not shown in attached file)
• - bold font is Helvetica Compressed
• - body copy (paragraphs) is Helvetica Medium
• - RGB equivalent of red is #ED1C24, which is the mix R 237, G 28, B 36
• However feel free to add other colors (e.g, golds, yellows, greys. etc.)
Nice to have
• I would like the design to be eye-catching, yet easy to read because it is a step-by-step instruction sheet. Feel free to use Icons. I have several more documents that also require updating, so I would prefer the look and feel of this doc to be transferable to other similar docs (e.g., FAQs, product descriptions, sales flyers.)
Should not have
• Do not change the written content or the order of the content. This is NOT a trifold doc.

```html
<!DOCTYPE html>
<html lang="en">
<head>
<meta charset="utf-8">
<title>TRV Collection and Shipping Info Sheet</title>
<link href="https://fonts.googleapis.com/css2?family=Anton&family=Arimo:wght@400;500&display=swap" rel="stylesheet">
<style>
  :root {
    --brand-red: #ff0000;
    --ink: #111111;
    --paper: #ffffff;
    --link: #2b5fd9;
  }
  * { margin: 0; padding: 0; box-sizing: border-box; }
  html, body { width: 873px; height: 1200px; overflow: hidden; background: var(--paper); }
  .sheet { position: relative; width: 873px; height: 1200px; font-family: "Arimo", Arial, sans-serif; color: var(--ink); }
  .timeline { position: absolute; left: 0; top: 0; }
  .step-badge { position: absolute; width: 122px; text-align: center; font-family: "Anton", "Arial Narrow", sans-serif; }
  .step-badge .label { display: block; color: var(--paper); font-size: 27px; line-height: 1; letter-spacing: -0.5px; }
  .step-badge .num { display: block; color: var(--ink); font-size: 86px; line-height: 0.95; }
  .copy { position: absolute; left: 196px; width: 646px; font-size: 17px; line-height: 22.7px; text-align: justify; }
  .alert { color: var(--brand-red); }
  .alert-lg { color: var(--brand-red); font-size: 19.5px; line-height: 25px; }
  .copy a { color: var(--link); }
  .contact-band { position: absolute; left: 0; top: 1033px; width: 873px; height: 167px; background: var(--brand-red); text-align: center; color: var(--paper); }
  .contact-band h2 { font-family: "Anton", "Arial Narrow", sans-serif; font-weight: 400; font-size: 37px; color: var(--ink); margin-top: 10px; line-height: 1.1; letter-spacing: -0.5px; }
  .contact-band p { font-size: 24px; line-height: 31px; }
  .contact-band a { color: var(--link); }
</style>
</head>
<body>
<div class="sheet">
  <svg class="timeline" width="873" height="1033" viewBox="0 0 873 1033">
    <g fill="none" stroke="#111" stroke-width="2">
      <path d="M85 0 V195 C130 195 158 225 158 270 H178"/>
      <path d="M85 330 V371 C130 371 158 401 158 446 H178"/>
      <path d="M85 506 V547 C130 547 158 577 158 622 H178"/>
      <path d="M85 682 V723 C130 723 158 753 158 798 H178"/>
      <path d="M85 858 V1033"/>
    </g>
    <g fill="#ff0000">
      <circle cx="85" cy="271" r="61"/>
      <circle cx="85" cy="446" r="61"/>
      <circle cx="85" cy="622" r="61"/>
      <circle cx="85" cy="798" r="61"/>
    </g>
  </svg>

  <div class="step-badge" style="left:24px;top:215px"><span class="label">STEP</span><span class="num">6</span></div>
  <div class="step-badge" style="left:24px;top:391px"><span class="label">STEP</span><span class="num">7</span></div>
  <div class="step-badge" style="left:24px;top:567px"><span class="label">STEP</span><span class="num">8</span></div>
  <div class="step-badge" style="left:24px;top:743px"><span class="label">STEP</span><span class="num">9</span></div>

  <p class="copy" style="top:13px"><span class="alert-lg">The manure sample must be fresh.</span> Ideally, collect the sample shortly after your horse has passed it. Parasitic matter deteriorates over time, which affects the test results. Schedule collection of samples in the morning if possible. Avoid collecting a manure sample that contains dirt, shavings, grass, etc. Select the sample from the top or middle of the manure pile. Avoid taking the sample from the portion of the pile touching the ground to minimize potential contamination.</p>

  <p class="copy" style="top:194px">DIG IN! Once you have identified your horse’s sample, turn the fecal collection bag inside out. A Step-by-Step Video is available at <a href="#">https://clearfieldpasturelabs.com/ blogs/news/our-sample-collection-bag</a>. With the label on the inside of the bag, place your hand inside the bag and collect the fecal nugget of choice. Ideally, the sample size should be larger than a golf ball but smaller than a tennis ball. Carefully return the bag right-side-out by using your other hand to pull the bag back over the hand grasping the sample.</p>

  <p class="copy" style="top:378px">REMOVE AS MUCH AIR AS POSSIBLE AND SEAL THE FECAL COLLECTION BAG SECURELY. Elimination of air from the fecal collection bag helps to preserve the sample and prevents parasitic eggs from hatching. Parasite eggs are anaerobic (living in the absence of air or oxygen) and removing excess air from the bag keeps them alive longer. <span class="alert-lg">Make certain the bag is completely sealed to avoid leakage.</span></p>

  <p class="copy" style="top:555px">Place the sealed Fecal Collection Bag in the Pre-Addressed Shipping Thermal Bubble Mailer. If you are not able to ship your sample on the same day it is collected, simply place the Pre-Addressed Shipping Thermal Bubble Mailer with the sample in the refrigerator (&lt;39 Fo), until you are ready to ship it. Remember, DO NOT FREEZE the sample.<br><span class="alert-lg">Only use the Clearfield Pasture Labs packaging provided. Do not substitute.</span></p>

  <p class="copy" style="top:718px">Immediately prior to shipping, retrieve the Gel Refrigerant Pack from the freezer and place it inside the Pre-Addressed Shipping Thermal Bubble Mailer, next to the sealed Fecal Collection Bag. For the Lab to process your sample in a timely manner, ship the sample early in the week to ensure receipt by the Lab prior to the weekend. It is highly recommended that your sample arrive at the lab within two days of its collection.<br><span class="alert">Do NOT place the Fecal Collection Bag in the freezer. Avoid exposure to excessive cold or heat.</span><br>After the Lab receives your horse’s fecal sample, a test will be performed to analyze and calculate your horse’s parasite burden. You will receive a detailed report summarizing the type and number of eggs found in the sample. Depending on your preferences indicated on your Equine Parasite Collection &amp; Treatment Form, the results will be emailed or sent via US Postal Service.</p>

  <footer class="contact-band">
    <h2>Any question?</h2>
    <p>Email us at <a href="#">mreyes@clearfieldlabs.com</a> or call 555-014-2286.</p>
    <p>Please check <a href="#">https://www.socialhub.com/clearfieldlabs/</a> for store hours.</p>
    <p>Additional test kits are always available at <a href="#">www.ClearfieldLabs.com</a></p>
  </footer>
</div>
</body>
</html>
```